Technology management company looking for a new website with a professional look

Brennick IT is a recently re-branded technology management company that is looking for a website design to match its personalized approach and friendly culture.

We would like to see a specialized, but related, page style for each of our main service offerings of:

• Commercial IT Support (This is our primary focus)
• Commercial Phone Systems (We partner with http://www.voxtrell.com/ for our phone systems)
• Point of Sale Systems (We partner with http://www.tillmora.com/ for our POS systems.
• Web Design
• Hollow Pine Computers (Our residential computer service offering, branded as Hollow Pine Computers)

The Hollow Pine Computers page should be build upon the Hollow Pine Computers logo, the other four pages should be branded as Brennick IT.

These five separate pages should have subtle, yet clearly defined links to one another. They should also each have a Home, Products, Service, and Company in the menu.

The website should have a clean design with professional appeal, but not appear too sterile or uninviting. It needs to have a simple, easy to navigate menu interface along the top. We would also like the site to be mobile friendly.

It should also allow us to easily tie in links to our social media pages (Facebook, LinkedIn, Twitter and Google+) and provide easy access to our contact information from each page.

This is a link to our old website www.hollowpinecomputers.com

We don't currently have copy available. The text and menu design should be easily editable and expandable so we can use the design to fit our copy.

In general we are looking for a concept we can modify to fit our needs.

We need this design to be available with layers in a .psd format.

Target Market(s)

Small to mid-size businesses.

Industry/Entity Type

Information Technology

Number of Pages Required

5+ page

Font styles to use
Sans Serif

Requirements
Must have
• Mobile Friendly
• Professional Type Face
• Unity between all pages
• .PSD Format
Nice to have
• Themed with our logo
Should not have
• Bubbly unprofessional typeface. No comic sans.

```html
<!DOCTYPE html>
<html lang="en">
<head>
<meta charset="utf-8">
<title>Hollow Pine Computers</title>
<link rel="stylesheet" href="https://fonts.googleapis.com/css2?family=Open+Sans:wght@300;400;600;700&family=Roboto+Condensed:wght@400;700&display=swap">
<style>
:root{
  --orange:#f26522;
  --orange-dark:#d9531a;
  --navy:#1d3b6b;
  --navy-dark:#13294d;
  --ink:#333;
  --muted:#888;
  --line:#e3e3e3;
  --footer:#0e0e0e;
  --footer-text:#9a9a9a;
  --white:#fff;
}
*{box-sizing:border-box;margin:0;padding:0}
html,body{width:1200px;height:2252px;overflow:hidden}
body{font-family:"Open Sans",sans-serif;color:var(--ink);background:var(--white);font-size:12px}
.site-header{height:48px;display:flex;align-items:center;justify-content:space-between;padding:0 168px;background:var(--white);border-bottom:1px solid var(--line)}
.brand{display:flex;align-items:center;gap:8px;font-weight:700;font-size:15px;color:var(--navy)}
.brand-mark{width:22px;height:22px;background:var(--navy);border-radius:50%}
.main-nav{display:flex;gap:22px;font-size:10px;font-weight:600;color:var(--ink);text-transform:uppercase;align-items:center}
.main-nav .active{color:var(--orange)}
.login-btn{background:var(--orange);color:var(--white);padding:4px 10px;border-radius:2px}
.hero{position:relative;height:392px;background:linear-gradient(100deg,#3a3d42 0%,#70757b 45%,#a9adb1 70%,#5b5f64 100%);text-align:center;color:var(--white)}
.hero-headline{padding-top:40px;font-size:32px;font-weight:600;line-height:1.3;text-shadow:0 1px 3px rgba(0,0,0,.4)}
.hero-headline em{font-style:normal;color:var(--orange)}
.scroll-mouse{position:absolute;left:50%;top:320px;transform:translateX(-50%)}
.main{position:relative;height:1280px;padding:56px 0 0 168px;display:flex;gap:10px}
.content{width:652px}
.sidebar{width:200px}
.intro{text-align:center}
.intro h1{font-weight:300;font-size:30px;color:var(--navy)}
.intro p{margin:14px auto 0;width:420px;font-size:11px;color:var(--muted);line-height:1.6}
.services{display:flex;gap:40px;margin-top:36px;padding:0 40px}
.service{flex:1;text-align:center}
.service h3{margin-top:10px;font-size:13px;font-weight:700;color:var(--navy)}
.service p{margin-top:8px;font-size:10px;color:var(--muted);line-height:1.6}
.feature-boxes{display:flex;gap:16px;margin-top:80px}
.feature{flex:1;height:260px;padding:20px 22px;background:linear-gradient(160deg,#e9e9e9,#c9cbcd);}
.feature h2{font-family:"Roboto Condensed",sans-serif;font-size:28px;font-weight:700;color:var(--ink);line-height:1}
.feature .tagline{font-family:"Roboto Condensed",sans-serif;font-size:17px;color:var(--orange);margin-top:4px}
.feature p{margin-top:14px;font-size:10px;line-height:1.6;color:#555}
.btn{display:inline-block;background:var(--orange);color:var(--white);font-size:10px;padding:6px 14px;border-radius:2px;margin-top:16px}
.gallery-head{text-align:center;margin-top:40px}
.gallery-head .pre{font-size:22px;font-weight:300;color:var(--ink)}
.gallery-head h2{font-size:30px;font-weight:700;color:var(--ink);line-height:1.1}
.gallery-head .sub{font-size:10px;color:var(--muted);margin-top:4px}
.tabs{display:flex;gap:20px;margin-top:28px;font-size:10px;color:var(--muted);align-items:center}
.tabs .current{background:var(--orange);color:var(--white);padding:5px 10px}
.grid{display:grid;grid-template-columns:repeat(4,1fr);gap:20px 14px;margin-top:22px}
.grid div{height:140px;background:linear-gradient(160deg,#f4f4f4,#cfd3d8)}
.side-card{position:relative;height:120px;margin-bottom:8px;background:linear-gradient(150deg,#8e979f,#4a525a)}
.side-card span{position:absolute;left:0;right:0;bottom:0;padding:5px 8px;background:var(--navy);color:var(--white);font-size:9px;font-weight:700;text-transform:uppercase}
.side-card.accent span{background:var(--orange)}
.side-title{font-size:14px;font-weight:700;color:var(--navy);margin-top:12px}
.video{height:150px;margin-top:8px;background:linear-gradient(160deg,#2c3340,#0f1319)}
.tool{display:flex;align-items:center;justify-content:center;gap:8px;height:60px;margin-top:18px;font-size:15px;font-weight:700;color:var(--navy)}
.tool .dot{width:20px;height:20px;border-radius:50%;background:var(--navy)}
.tool.status{background:var(--navy);color:var(--white);font-size:13px;height:40px}
.newsletter{height:128px;background:linear-gradient(90deg,var(--navy-dark),var(--navy));padding:32px 168px;color:var(--white)}
.newsletter h2{font-size:16px;font-weight:400}
.news-form{display:flex;gap:10px;margin-top:14px}
.news-form div{flex:1;height:30px;background:rgba(255,255,255,.1);border-bottom:1px solid rgba(255,255,255,.4);font-size:10px;padding:9px;color:#ccc}
.news-form span{background:var(--orange);padding:9px 18px;font-size:10px}
.site-footer{position:relative;height:404px;background:var(--footer);color:var(--footer-text);padding:36px 60px 0}
.footer-cols{display:flex;gap:60px}
.footer-col{width:230px;font-size:10px;line-height:1.7}
.footer-col h4{color:var(--white);font-size:11px;font-weight:600;margin-bottom:12px}
.contact-row{display:flex;gap:8px;margin-bottom:10px}
.field{height:22px;background:#222;margin-bottom:8px;padding:4px 6px}
.field.area{height:60px}
.submit{display:inline-block;background:var(--orange);color:var(--white);padding:4px 14px}
.partners{display:grid;grid-template-columns:repeat(2,90px);gap:10px}
.partners div{height:34px;background:#d8d8d8}
.footer-brand{position:absolute;right:80px;top:290px;display:flex;align-items:center;gap:8px;font-size:24px;font-weight:700;color:var(--white)}
.footer-brand i{width:24px;height:24px;background:var(--orange)}
.live-chat{position:absolute;right:80px;top:340px;background:var(--orange);color:var(--white);font-size:11px;padding:6px 30px}
.copyright{position:absolute;left:60px;bottom:10px;font-size:9px}
</style>
</head>
<body>
<header class="site-header">
  <div class="brand"><span class="brand-mark"></span>Hollow Pine Computers</div>
  <nav class="main-nav"><span class="active">Home</span><span>Products</span><span>Services ▾</span><span>Company</span><span class="login-btn">Login ▾</span></nav>
</header>

<section class="hero" role="img" aria-label="Greyscale photo of a smiling man at a computer">
  <h2 class="hero-headline">Temporibus autem <em>quibusdam</em><br>perferendis doloribus <em>asperiores</em></h2>
  <svg class="scroll-mouse" width="20" height="32" viewBox="0 0 20 32"><rect x="1" y="1" width="18" height="30" rx="9" fill="none" stroke="#fff" stroke-width="2"/><rect x="9" y="7" width="2" height="7" fill="#fff"/></svg>
</section>

<main class="main">
  <div class="content">
    <div class="intro">
      <h1>We Are Hollow Pine Computers</h1>
      <p>Our goal is to build a relationship with our clients, communicate clearly, and find timely, cost effective solutions to your needs.</p>
    </div>
    <div class="services">
      <div class="service">
        <svg width="46" height="40" viewBox="0 0 46 40"><path d="M4 20 L23 4 L42 20" fill="none" stroke="#f26522" stroke-width="4"/><rect x="11" y="19" width="24" height="19" fill="#f26522"/><rect x="20" y="26" width="6" height="12" fill="#fff"/></svg>
        <h3>Residential</h3>
        <p>We make house calls for all sorts of issues, whether you can't get on the internet or you need help installing your new printer.</p>
      </div>
      <div class="service">
        <svg width="46" height="40" viewBox="0 0 46 40"><rect x="6" y="8" width="14" height="30" fill="#f26522"/><rect x="24" y="2" width="16" height="36" fill="#f26522"/><rect x="28" y="8" width="3" height="3" fill="#fff"/><rect x="33" y="8" width="3" height="3" fill="#fff"/><rect x="28" y="16" width="3" height="3" fill="#fff"/><rect x="33" y="16" width="3" height="3" fill="#fff"/></svg>
        <h3>Commercial</h3>
        <p>We offer a wide variety of services for our commercial clients, depending on the scope of their business and needs.</p>
      </div>
    </div>

    <div class="feature-boxes">
      <div class="feature" role="img" aria-label="Office photo behind the about panel">
        <h2>About Hollow Pine</h2>
        <div class="tagline">Top-quality IT service</div>
        <p>We place a high value on our relationship with our customers, communicating clearly and finding the best solution for every home and office we serve.</p>
        <span class="btn">Read More</span>
      </div>
      <div class="feature" role="img" aria-label="Computer hardware photo behind the products panel">
        <h2>Our Products</h2>
        <div class="tagline">Making your technology</div>
        <p>We carry a wide selection of hardware and components for our clients, and we source reliable gear suited to each setup and budget.</p>
        <span class="btn">Read More</span>
      </div>
    </div>

    <div class="gallery-head">
      <div class="pre">View our</div>
      <h2>Products Gallery</h2>
      <div class="sub">Professional Services Customized</div>
    </div>
    <div class="tabs"><span class="current">All</span><span>Desktops</span><span>Laptops</span><span>Monitors</span><span>Printers</span><span>Cables</span><span>PC peripherals</span></div>
    <div class="grid">
      <div role="img" aria-label="Desktop computer"></div>
      <div role="img" aria-label="Laptop"></div>
      <div role="img" aria-label="Monitors"></div>
      <div role="img" aria-label="Headset"></div>
      <div role="img" aria-label="Cables"></div>
      <div role="img" aria-label="Printer"></div>
      <div role="img" aria-label="Laptop keyboard"></div>
      <div role="img" aria-label="Tablet"></div>
    </div>
  </div>

  <aside class="sidebar">
    <div class="side-card" role="img" aria-label="Office team at work"><span>Commercial IT Support</span></div>
    <div class="side-card accent" role="img" aria-label="Desk phone"><span>Commercial Phone Systems</span></div>
    <div class="side-card" role="img" aria-label="Checkout terminal"><span>Point of Sale Systems</span></div>
    <div class="side-card accent" role="img" aria-label="Website on a screen"><span>Web Design</span></div>
    <div class="side-card" role="img" aria-label="Shop storefront"><span>Hollow Pine Computers</span></div>
    <div class="side-title">Our Video</div>
    <div class="video" role="img" aria-label="Video player"></div>
    <div class="tool"><span class="dot"></span>Linkwell</div>
    <div class="tool status">
      <svg width="16" height="16" viewBox="0 0 16 16"><path d="M3 8 L7 12 L13 4" fill="none" stroke="#fff" stroke-width="2"/></svg>Repair Status</div>
    <div class="tool">
      <svg width="18" height="18" viewBox="0 0 18 18"><rect x="1" y="2" width="16" height="11" fill="none" stroke="#1d3b6b" stroke-width="2"/><rect x="6" y="14" width="6" height="2" fill="#1d3b6b"/></svg>Remote</div>
  </aside>
</main>

<section class="newsletter">
  <h2>Subscribe to our Newsletter</h2>
  <div class="news-form"><div>Email</div><span>SUBSCRIBE</span></div>
</section>

<footer class="site-footer">
  <div class="footer-cols">
    <div class="footer-col">
      <h4>Contact Information</h4>
      <div class="contact-row"><svg width="12" height="14" viewBox="0 0 12 14"><path d="M6 1a4 4 0 0 1 4 4c0 3-4 8-4 8S2 8 2 5a4 4 0 0 1 4-4z" fill="#f26522"/></svg><span>Address:<br>214 Fernhill Road<br>Alder Falls, OR 97100</span></div>
      <div class="contact-row"><svg width="12" height="12" viewBox="0 0 12 12"><path d="M2 1h3l1 3-2 1a7 7 0 0 0 3 3l1-2 3 1v3c-6 0-9-3-9-9z" fill="#f26522"/></svg><span>Phone:<br>(555) 018-2244</span></div>
      <div class="contact-row"><svg width="12" height="10" viewBox="0 0 12 10"><rect x="0" y="0" width="12" height="10" fill="#f26522"/><path d="M0 0 L6 5 L12 0" fill="none" stroke="#0e0e0e"/></svg><span>Email:<br>help@hollowpine.example</span></div>
      <div class="contact-row"><svg width="12" height="12" viewBox="0 0 12 12"><circle cx="6" cy="6" r="5" fill="none" stroke="#f26522" stroke-width="2"/><path d="M6 3v3h2" stroke="#f26522" fill="none"/></svg><span>Working Days/Hours:<br>Mon - Fri 8:00 AM - 5:00 PM</span></div>
    </div>
    <div class="footer-col">
      <h4>Quick Contact</h4>
      <div class="field">Name</div>
      <div class="field">Email</div>
      <div class="field area">Message</div>
      <span class="submit">Submit</span>
    </div>
    <div class="footer-col">
      <h4>Our Partners</h4>
      <div class="partners"><div></div><div></div><div></div><div></div><div></div><div></div></div>
    </div>
    <div class="footer-col">
      <h4>Links</h4>
      <div>Home<br>Products<br>Services<br>Company<br>Contact</div>
    </div>
  </div>
  <div class="footer-brand"><i></i>Brennick IT</div>
  <span class="live-chat">Live Chat</span>
  <div class="copyright">Copyright © Hollow Pine Computers</div>
</footer>
</body>
</html>
```